RPN FORMED

building services
decks
pergola
renovation
extensions
general building

Target Market(s)

middle to upper class

Industry/Entity Type

building

Contact Information for Business Card

my details 0438917264 tkbarrow47@mailvora.com BLD581047

Font styles to use
Serif

Colors
00AB8E
00BBA5
67D7C9
C6EFE9
E9F9F6

Requirements
Must have
• logo on the front and details on the back
Nice to have
• sharp and clean lines

```html
<!DOCTYPE html>
<html lang="en">
<head>
<meta charset="utf-8">
<title>RPN Formed – Business Card</title>
<link rel="stylesheet" href="https://fonts.googleapis.com/css2?family=Tinos:wght@400;700&family=Jost:wght@400&display=swap">
<style>
  :root {
    --teal: #14ae92;
    --ink: #1a1a1a;
    --paper: #ffffff;
    --backdrop: #d4d5d8;
  }
  * { margin: 0; padding: 0; box-sizing: border-box; }
  html, body {
    width: 1200px; height: 1200px; overflow: hidden;
    background: var(--backdrop);
  }
  .stage { position: relative; width: 1200px; height: 1200px; }
  .card {
    position: absolute; top: 480px;
    width: 421px; height: 240px;
  }
  .card--details { left: 154px; background: var(--paper); }
  .card--brand { left: 625px; background: var(--teal); }

  .wordmark {
    font-family: "Tinos", serif; font-weight: 700;
    line-height: 1.05; letter-spacing: 0.08em;
  }
  .card--details .wordmark {
    position: absolute; left: 15px; top: 24px;
    color: var(--teal); font-size: 30px;
  }
  .card--brand .wordmark {
    position: absolute; left: 0; right: 0; top: 50%;
    transform: translateY(-50%);
    text-align: center; color: var(--paper); font-size: 44px;
  }
  .wordmark span { display: block; }

  .services {
    position: absolute; right: 17px; top: 18px;
    list-style: none; text-align: right;
    font-family: "Tinos", serif; font-size: 11px;
    line-height: 14.3px; color: var(--ink);
  }
  .services li::after {
    content: ""; display: inline-block;
    width: 8px; height: 8px; margin-left: 8px;
    border-radius: 50%; background: var(--teal);
    vertical-align: -0.5px;
  }
  .divider {
    position: absolute; left: 15px; right: 17px; top: 136px;
    height: 1px; background: var(--ink);
  }
  .contact {
    position: absolute; right: 17px; top: 165px;
    text-align: right; font-family: "Jost", sans-serif;
    color: var(--ink);
  }
  .contact .line { font-size: 11.5px; line-height: 14px; }
  .contact .licence { font-size: 16px; line-height: 20px; margin-top: 3px; }
</style>
</head>
<body>
<main class="stage">
  <section class="card card--details">
    <div class="wordmark"><span>RPN</span><span>FORMED</span></div>
    <ul class="services">
      <li>BUILDING SERVICES</li>
      <li>DECKS</li>
      <li>PERGOLA</li>
      <li>RENOVATION</li>
      <li>EXTENSIONS</li>
      <li>GENERAL BUILDING</li>
    </ul>
    <div class="divider"></div>
    <div class="contact">
      <p class="line">043 891 7264</p>
      <p class="line">tkbarrow47@mailvora.com</p>
      <p class="licence">BLD581047</p>
    </div>
  </section>
  <section class="card card--brand">
    <div class="wordmark"><span>RPN</span><span>FORMED</span></div>
  </section>
</main>
</body>
</html>
```